New Business Card

Would like a shiny card with Metallic logo raised on th front. Address 418 Kestwick Lane, Toronto Ontario M4T2B8, phone 416 555 0382, email kmvc@lorentel.ca and web www.kmvc.ca on the back in right and left lower corners balanced. Top of back should say Personalized Care for Pet's and their People centered. Leaving space on the back to write. Horizontal placement

```html
<!DOCTYPE html>
<html lang="en">
<head>
<meta charset="utf-8">
<title>Kestwick Mews Veterinary Clinic – Business Card</title>
<link rel="stylesheet" href="https://fonts.googleapis.com/css2?family=Open+Sans:wght@400;600;700&family=PT+Serif&display=swap">
<style>
  :root {
    --page: #e9e9e9;
    --ink: #111111;
    --paper: #ffffff;
    --silver: #c8c8c8;
    --rule: #333333;
    --muted: #444444;
  }
  * { box-sizing: border-box; margin: 0; padding: 0; }
  html, body { width: 1200px; height: 1200px; overflow: hidden; }
  body {
    background: var(--page);
    font-family: "Open Sans", sans-serif;
    color: var(--ink);
    position: relative;
  }
  .card {
    position: absolute;
    left: 250px;
    width: 700px;
    height: 400px;
    box-shadow: 0 6px 18px rgba(0,0,0,0.18);
    overflow: hidden;
  }

  /* Front */
  .card-front { top: 100px; background: var(--ink); }
  .brand {
    position: absolute;
    left: 0; right: 0; top: 150px;
    display: flex; flex-direction: column; align-items: center; gap: 18px;
  }
  .brand-dot {
    width: 46px; height: 46px; border-radius: 50%;
    background: var(--silver);
  }
  .brand-name {
    font-weight: 600;
    font-size: 30px;
    letter-spacing: 3px;
    color: var(--silver);
    text-transform: uppercase;
  }

  /* Back */
  .card-back { top: 600px; background: var(--paper); }
  .tagline-band {
    position: absolute; left: 0; right: 0; top: 24px; height: 40px;
    background: var(--ink);
    color: var(--paper);
    font-weight: 700; font-size: 19px; letter-spacing: 0.3px;
    display: flex; align-items: center; padding-left: 28px;
    text-transform: uppercase;
  }
  .field {
    position: absolute;
    border-bottom: 1.5px solid var(--rule);
    font-family: "PT Serif", serif;
    font-size: 12px;
    letter-spacing: 1px;
    color: var(--muted);
    text-transform: uppercase;
    height: 22px;
  }
  .field-name { left: 28px; right: 28px; top: 80px; }
  .field-date { left: 28px; right: 28px; top: 120px; }
  .field-time { left: 330px; right: 28px; top: 190px; }
  .field-blank { left: 330px; right: 28px; top: 232px; border-bottom: 1.5px solid var(--rule); }

  .contact {
    position: absolute; left: 28px; top: 172px;
    font-size: 15px; line-height: 1;
    display: flex; flex-direction: column; gap: 10px;
  }
  .contact-line { display: flex; align-items: center; gap: 8px; }
  .contact-line svg { width: 14px; height: 14px; fill: var(--ink); }
  .contact-rule {
    position: absolute; left: 0; top: 236px; width: 300px; height: 10px;
    background: var(--ink);
  }
  .web {
    position: absolute; left: 28px; top: 266px;
    font-weight: 700; font-size: 20px; letter-spacing: 1.5px;
  }
  .footer-block {
    position: absolute; left: 300px; bottom: 0; width: 110px; height: 120px;
    background: var(--ink);
  }
  .footer-band {
    position: absolute; left: 300px; right: 0; bottom: 0; height: 44px;
    background: var(--ink);
  }
  .address {
    position: absolute; right: 28px; top: 262px;
    font-size: 18px; line-height: 1.3;
    display: flex; align-items: flex-end; gap: 8px;
    text-align: right;
  }
  .address svg { width: 14px; height: 18px; fill: var(--ink); margin-bottom: 4px; }
</style>
</head>
<body>

<section class="card card-front" aria-label="Card front">
  <div class="brand">
    <span class="brand-dot"></span>
    <span class="brand-name">Kestwick Mews Veterinary Clinic</span>
  </div>
</section>

<section class="card card-back" aria-label="Card back">
  <div class="tagline-band">Personalized care for pet's and their people centered</div>

  <div class="field field-name">Name:</div>
  <div class="field field-date">Date:</div>

  <div class="contact">
    <div class="contact-line">
      <svg viewBox="0 0 24 24" aria-hidden="true"><path d="M6.6 10.8a15.1 15.1 0 0 0 6.6 6.6l2.2-2.2a1 1 0 0 1 1-.25 11.4 11.4 0 0 0 3.6.57 1 1 0 0 1 1 1V20a1 1 0 0 1-1 1A17 17 0 0 1 3 4a1 1 0 0 1 1-1h3.5a1 1 0 0 1 1 1c0 1.25.2 2.45.57 3.57a1 1 0 0 1-.25 1z"/></svg>
      <span>416 555 0382</span>
    </div>
    <div class="contact-line">
      <svg viewBox="0 0 24 24" aria-hidden="true"><path d="M2 5h20v14H2z M4 7v.5l8 5 8-5V7z" fill-rule="evenodd"/></svg>
      <span>kmvc@lorentel.ca</span>
    </div>
  </div>
  <div class="contact-rule"></div>
  <div class="web">www.kmvc.ca</div>

  <div class="field field-time">Time:</div>
  <div class="field-blank field"></div>

  <div class="address">
    <span>418 Kestwick Lane<br>Toronto Ontario M4T2B8</span>
    <svg viewBox="0 0 24 30" aria-hidden="true"><path d="M12 0a10 10 0 0 0-10 10c0 7.5 10 20 10 20s10-12.5 10-20A10 10 0 0 0 12 0zm0 14a4 4 0 1 1 0-8 4 4 0 0 1 0 8z"/></svg>
  </div>

  <div class="footer-block"></div>
  <div class="footer-band"></div>
</section>

</body>
</html>
```